Business Card for: Keelwright Financial Advisory Services Inc.

provide strategic financial advisory services to companies in the areas of corporate finance, mergers and acquisitions, executive coaching and strategic planning

Target Market(s)

Companies, banks, accountants, lawyers

Industry/Entity Type

High end business consulting in corporate finance, mergers and acquisitions, consulting

Contact Information for Business Card

Name of company, Name: xxxxxx xxxxxx , CEO, - phone number: 1-xxx-xxx-xxxx, - email address,

Requirements
Must have
• Must be professional and simple.
Nice to have
• simple, straight graphics, must give the impression that we are trustworthy, professional, competent
Should not have
• loud colors, loud design features

```html
<!DOCTYPE html>
<html lang="en">
<head>
<meta charset="utf-8">
<title>Keelwright Financial Advisory Services Inc. – Business Card</title>
<link rel="stylesheet" href="https://fonts.googleapis.com/css2?family=Outfit:wght@300;400;500;700&display=swap">
<style>
  :root {
    --backdrop: #4d4d4d;
    --card-deep: #0077b6;
    --card-bright: #3bbfe0;
    --card-mid: #0396c8;
    --accent-cyan: #48cae4;
    --ink-light: #ffffff;
    --card-shadow: rgba(0, 0, 0, 0.85);
  }
  * { margin: 0; padding: 0; box-sizing: border-box; }
  html, body {
    width: 1093px;
    height: 1200px;
    overflow: hidden;
    background: var(--backdrop);
    font-family: "Outfit", sans-serif;
    color: var(--ink-light);
  }
  .stage {
    position: relative;
    width: 1093px;
    height: 1200px;
  }
  .card {
    position: absolute;
    left: 265px;
    border-radius: 27px;
    box-shadow: 3px 4px 3px var(--card-shadow);
    overflow: hidden;
  }
  .card--front {
    top: 226px;
    width: 577px;
    height: 356px;
    background: var(--card-deep);
  }
  .card__feature {
    position: absolute;
    left: 234px;
    top: 0;
    right: 0;
    bottom: 0;
    border-top-left-radius: 60% 40%;
    border-bottom-left-radius: 100% 45%;
    background: linear-gradient(135deg, var(--accent-cyan) 0%, #9fe2f2 45%, var(--ink-light) 80%);
  }
  .card__feature-base {
    position: absolute;
    right: 0;
    bottom: 0;
    width: 43px;
    height: 60px;
    background: var(--ink-light);
  }
  .holder {
    position: absolute;
    left: 30px;
    top: 186px;
  }
  .holder__name {
    font-size: 29px;
    font-weight: 400;
    line-height: 1;
    letter-spacing: 0.2px;
  }
  .holder__name strong { font-weight: 700; }
  .holder__role {
    margin-top: 2px;
    font-size: 19px;
    font-weight: 400;
    line-height: 1.1;
  }
  .contacts {
    position: absolute;
    left: 25px;
    top: 256px;
    list-style: none;
  }
  .contacts__item {
    display: flex;
    align-items: center;
    height: 26.5px;
    font-size: 19.5px;
    font-weight: 400;
  }
  .contacts__icon {
    width: 24px;
    height: 24px;
    margin-right: 4px;
    flex: none;
  }
  .card--back {
    top: 621px;
    width: 581px;
    height: 357px;
    background: linear-gradient(to top right, var(--card-deep) 0%, var(--card-mid) 55%, var(--card-bright) 100%);
    display: flex;
    align-items: center;
    justify-content: center;
  }
  .brand {
    text-align: center;
    font-weight: 500;
    line-height: 1.05;
    margin-top: 80px;
  }
  .brand__name {
    display: block;
    font-size: 58px;
    letter-spacing: -0.5px;
  }
  .brand__line {
    display: block;
    font-size: 22px;
    margin-top: 4px;
  }
</style>
</head>
<body>
<main class="stage">
  <section class="card card--front" aria-label="Business card front">
    <div class="card__feature" role="img" aria-label="Large brand decoration area in white and light cyan"></div>
    <div class="card__feature-base" aria-hidden="true"></div>
    <div class="holder">
      <p class="holder__name">Marcus <strong>Hale</strong></p>
      <p class="holder__role">CEO</p>
    </div>
    <ul class="contacts">
      <li class="contacts__item">
        <svg class="contacts__icon" viewBox="0 0 24 24" aria-hidden="true">
          <circle cx="12" cy="12" r="12" fill="#fff"/>
          <path d="M8.2 6.5l2 2.2-1.1 1.4c.8 1.8 2 3 3.8 3.8l1.4-1.1 2.2 2-1.2 1.6c-3.6-.4-7.1-3.9-7.5-7.5z" fill="var(--card-deep)"/>
        </svg>
        <span>044-987 650 312</span>
      </li>
      <li class="contacts__item">
        <svg class="contacts__icon" viewBox="0 0 24 24" aria-hidden="true">
          <circle cx="12" cy="12" r="12" fill="#fff"/>
          <rect x="6" y="8" width="12" height="8.5" fill="none" stroke="var(--card-deep)" stroke-width="1.3"/>
          <path d="M6 8l6 5 6-5M6 16.5l4.5-4M18 16.5l-4.5-4" fill="none" stroke="var(--card-deep)" stroke-width="1.1"/>
        </svg>
        <span>info@keelwright.com</span>
      </li>
      <li class="contacts__item">
        <svg class="contacts__icon" viewBox="0 0 24 24" aria-hidden="true">
          <circle cx="12" cy="12" r="12" fill="#fff"/>
          <g fill="none" stroke="var(--card-deep)" stroke-width="1.1">
            <circle cx="12" cy="12" r="6"/>
            <ellipse cx="12" cy="12" rx="2.6" ry="6"/>
            <path d="M6 12h12M7 9h10M7 15h10"/>
          </g>
        </svg>
        <span>www.keelwright.com</span>
      </li>
    </ul>
  </section>

  <section class="card card--back" aria-label="Business card back">
    <p class="brand">
      <span class="brand__name">Keelwright</span>
      <span class="brand__line">Financial Advisory Services Inc.</span>
    </p>
  </section>
</main>
</body>
</html>
```